Harborline Energy - needs a business card

Harborline Energy is a U.S. based diesel sourcing and distribution company that supports American oil & gas fields through providing quality product and consistent services.

Target Market(s)

Oil and Gas

Contact Information for Business Card

The background of the card must be white to ensure the logo pops.

Font styles to use
Serif
Sans Serif

Colors

Designer to choose colors to be used in the design.

Requirements
Must have
• Front of Card: Tag line: Harborline Energy, Powering America's Oil & Gas fields.
• Not sure if you guys do this part but just in case...
• Dale Menschow
• Owner/CEO
• C:555.318.4076
• E:Dmenschow@harborlineenergy.example
• W:Harborlineenergy.example
• Locations: Servicing the Powder River, DJ basin and Bakken formations.
• Back of Card: " Frac fueling is what we do. We understand how important diesel fuel is to your operation, which is why our main service line is Frac fueling. We assure our supply and stand by our service"

```html
<!DOCTYPE html>
<html lang="en">
<head>
<meta charset="utf-8">
<title>Harborline Energy – Business Card</title>
<link href="https://fonts.googleapis.com/css2?family=Open+Sans:wght@400;600;700&display=swap" rel="stylesheet">
<style>
  :root {
    --navy: #1f3a6e;
    --red: #c8262e;
    --ink: #4a4a4a;
    --muted: #6b6b6b;
    --paper: #ffffff;
    --stage: #e4e5e8;
  }
  * { margin: 0; padding: 0; box-sizing: border-box; }
  html, body { width: 1200px; height: 900px; overflow: hidden; }
  body {
    background: var(--stage);
    font-family: "Open Sans", Arial, sans-serif;
    display: flex;
    flex-direction: column;
    align-items: center;
    justify-content: center;
    gap: 36px;
  }
  .card {
    position: relative;
    width: 700px;
    height: 400px;
    background: var(--paper);
    overflow: hidden;
    box-shadow: 0 6px 18px rgba(0,0,0,.18);
  }

  /* Front */
  .front .brand {
    position: absolute;
    left: 50px; top: 160px;
    width: 230px;
    display: flex; align-items: center; gap: 14px;
  }
  .brand-dot {
    width: 34px; height: 34px; border-radius: 50%;
    background: var(--navy);
    flex: none;
  }
  .brand-name {
    color: var(--navy);
    font-weight: 700;
    font-size: 28px;
    line-height: 1.1;
    letter-spacing: .5px;
    text-transform: uppercase;
  }
  .front .divider {
    position: absolute;
    left: 300px; top: 70px;
    width: 1.5px; height: 230px;
    background: var(--red);
  }
  .details {
    position: absolute;
    left: 324px; top: 70px;
    width: 350px;
    color: var(--ink);
  }
  .person-name { font-size: 28px; font-weight: 400; color: var(--muted); line-height: 1.1; }
  .person-name .first { color: var(--red); font-weight: 700; text-transform: uppercase; }
  .person-role { font-size: 17px; color: var(--muted); margin-top: 4px; }
  .service-area { font-size: 17px; color: var(--red); line-height: 1.3; margin-top: 16px; }
  .contact-list { list-style: none; margin-top: 20px; font-size: 16px; color: var(--ink); }
  .contact-list li { display: flex; align-items: center; gap: 10px; line-height: 1.7; white-space: nowrap; }
  .contact-list svg { width: 16px; height: 16px; flex: none; }
  .contact-list .web-accent { color: var(--red); }

  /* Back */
  .back .blurb {
    position: absolute;
    left: 44px; top: 40px;
    width: 380px;
    font-size: 14.5px;
    line-height: 1.45;
    color: var(--muted);
  }
  .back .lockup { position: absolute; left: 44px; top: 205px; }
  .back .brand-name { font-size: 34px; }
  .back .lockup-rule { width: 300px; height: 2px; background: var(--red); margin-top: 8px; }
  .tagline { margin-top: 8px; font-size: 15.5px; color: var(--navy); }
  .back .mark-panel {
    position: absolute; right: 0; top: 0;
    width: 330px; height: 400px;
  }
</style>
</head>
<body>

  <section class="card front" aria-label="Business card front">
    <div class="brand">
      <span class="brand-dot"></span>
      <span class="brand-name">Harborline<br>Energy</span>
    </div>
    <div class="divider"></div>
    <div class="details">
      <p class="person-name"><span class="first">Dale</span> Menschow</p>
      <p class="person-role">Owner | CEO</p>
      <p class="service-area">Servicing the Powder River<br>DJ basin and Bakken formations</p>
      <ul class="contact-list">
        <li>
          <svg viewBox="0 0 24 24" aria-hidden="true"><path fill="var(--red)" d="M6.6 10.8a15.1 15.1 0 0 0 6.6 6.6l2.2-2.2a1 1 0 0 1 1-.25 11.4 11.4 0 0 0 3.6.57 1 1 0 0 1 1 1V20a1 1 0 0 1-1 1A17 17 0 0 1 3 4a1 1 0 0 1 1-1h3.5a1 1 0 0 1 1 1c0 1.250.2 2.45.57 3.57a1 1 0 0 1-.25 1z"/></svg>
          555.318.4076
        </li>
        <li>
          <svg viewBox="0 0 24 24" aria-hidden="true"><rect x="2" y="5" width="20" height="14" rx="1.5" fill="var(--red)"/><path d="M3 6l9 7 9-7" fill="none" stroke="#fff" stroke-width="1.8"/></svg>
          Dmenschow@harborlineenergy.example
        </li>
        <li>
          <svg viewBox="0 0 24 24" aria-hidden="true"><circle cx="12" cy="12" r="10" fill="var(--red)"/><path d="M2 12h20M12 2c3 3 3 17 0 20M12 2c-3 3-3 17 0 20" fill="none" stroke="#fff" stroke-width="1.4"/></svg>
          <span>Harborline<span class="web-accent">energy</span>.example</span>
        </li>
      </ul>
    </div>
  </section>

  <section class="card back" aria-label="Business card back">
    <p class="blurb">Frac fueling is what we do. We understand how important diesel fuel is to your operation, which is why our main service line is Frac fueling. We assure our supply and stand by our service.</p>
    <div class="lockup">
      <span class="brand-name">Harborline Energy</span>
      <div class="lockup-rule"></div>
      <p class="tagline">Powering America's Oil &amp; Gas Fields</p>
    </div>
    <svg class="mark-panel" viewBox="0 0 330 400" role="img" aria-label="Large brand emblem area in navy and red">
      <path d="M330 0 V400 H40 C20 330 60 200 150 130 C220 80 290 40 330 0Z" fill="var(--navy)"/>
    </svg>
  </section>

</body>
</html>
```